Your Harbor Agent Website Design

Creative Brief: Website Design for Your Harbor Agent
- Project Overview: Design a website for our new brand, "Your Harbor Agent". Your Harbor Agent is a service that matches clients with the perfect realtor. The primary function of this site is to serve as a lead generation hub, to generate leads of people who are looking to either buy or sell their house and need a great realtor. The site needs to have a very clean, modern design using sites like Tallyquest, Brickwell, Lantern, and Vexomill as an example. The site also needs to have a primary lead capture capability through a multi-step form or questionnaire that indicates if they are buying or selling, and depending on that selection, creates two different flows.

Target Audience:
- Homebuyers and sellers in the Denver area
- Individuals looking for high-quality realtor services
- Users seeking a seamless and professional online & home buying/selling experience

Objectives:
- Create a visually appealing, modern website with a strong emphasis on lead generation.
- Design advanced, multi-step forms for efficient lead capture.
- Ensure the website is user-friendly and optimized for both desktop and mobile devices.

Pages to Design:
Home Page:
- Engaging hero section with a clear call to action and the ability to enter the form flow
- Brief introduction to Your Harbor Agent and its unique value proposition
- Key features & benefits of being matched with a realtor by Your Harbor Agent
- Testimonials and success stories
- Lead capture form

About Page:
- Overview of Your Harbor Agent’s mission and values
- Professional and trust-building imagery

How it Works Page:
- Step-by-step explanation of the matching process (complete the form and we will match you with a realtor)
- Visual aids (icons, graphics) to simplify complex information
- Customer journey map from inquiry to successful match & sale of home
- Lead capture form

Contact Us Page:
- Simple and accessible contact form
- Contact details
- Call to action for immediate inquiries

Blog Template:
- Clean, easy-to-read layout for blog posts, primarily location/neighborhood guides as well as standard blogs
- Sidebar for recent posts, categories, and tags
- Social sharing buttons
- Lead capture form embedded within blog posts

Design Style:
- Modern and professional with a focus on usability
- Clean lines and intuitive navigation
- Use of curved corners and minimal straight lines for a sleek look
- Incorporation of graphic design elements, potentially including 3D and isomorphic design
- Inspired by sites like Tallyquest, Brickwell, Lantern, and Vexomill
Consistent color scheme and typography

Visual References:
- Tallyquest: For its professional and corporate look
- Brickwell and Lantern: For their user-friendly interfaces and modern design
- Vexomill: For its clean and functional layout

Target Market(s)

- Homebuyers and sellers in the Denver area, Individuals looking for high-quality realtor services, Users seeking a seamless and professional home buying/selling experience

Industry/Entity Type

Real Estate

Number of Pages Required

5+ page

Requirements
Must have
• Fully designed website with lead capture functionality based on brief
Nice to have
• Designed in Figma, Starting / Placeholder copy

```html
<!DOCTYPE html>
<html lang="en">
<head>
<meta charset="utf-8">
<title>Harbor Agent — Buy your next home before you sell</title>
<link href="https://fonts.googleapis.com/css2?family=Inter:wght@400;500;600;700&family=Roboto:wght@400;500;700&display=swap" rel="stylesheet">
<style>
:root{
  --blue:#0a84f0;
  --ink:#0d0f1a;
  --muted:#6b7080;
  --soft:#f3f5f9;
  --white:#ffffff;
  --footer:#070b1f;
  --star:#f5a300;
  --sky:#e3ecf8;
  --sky-deep:#c4daf3;
  --leaf:#7db58a;
  --lilac:#d4d3e6;
}
*{margin:0;padding:0;box-sizing:border-box}
html,body{width:1200px;height:3295px;overflow:hidden}
body{position:relative;background:var(--white);font-family:Roboto,Arial,sans-serif;color:var(--ink)}
.abs{position:absolute}
.bg-shapes{position:absolute;left:0;top:0;width:1200px;height:3295px}
.logo{font-family:Inter,Arial,sans-serif;font-weight:700;font-size:20px;color:var(--ink)}
.nav-links{left:455px;top:52px;display:flex;gap:22px;font-size:14px;font-weight:500}
.login{left:867px;top:52px;font-size:14px;font-weight:500}
.btn-dark{left:926px;top:42px;width:131px;height:39px;border-radius:20px;background:var(--ink);color:#fff;font-size:14px;font-weight:500;display:flex;align-items:center;justify-content:center}
.btn-blue{background:var(--blue);color:#fff;border-radius:30px;display:flex;align-items:center;justify-content:center;font-weight:700;letter-spacing:.3px;gap:7px}
.hl{color:var(--blue)}
.hero-title{left:142px;top:192px;font-family:Inter,Arial,sans-serif;font-size:43px;font-weight:600;line-height:50px}
.hero-title .hl{font-weight:400}
.hero-text{left:144px;top:315px;width:420px;font-size:15px;line-height:25px;font-weight:400}
.section-title{font-family:Inter,Arial,sans-serif;font-weight:600;color:var(--ink)}
.about-text{left:623px;width:430px;font-size:13px;line-height:22.5px;color:var(--muted)}
.feature{font-size:17px;font-weight:700;white-space:nowrap}
.icon-badge{width:76px;height:76px;border-radius:50%;background:#fff;box-shadow:0 6px 18px rgba(20,40,90,.12);display:flex;align-items:center;justify-content:center}
.card{width:380px;height:214px;background:#fff;border-radius:34px;box-shadow:0 8px 22px rgba(20,30,60,.14)}
.card-photo{width:108px;height:108px;border-radius:50%}
.quote-mark{font-family:Georgia,serif;font-size:64px;font-weight:700;line-height:1}
.quote-text{font-size:13px;line-height:22px;color:var(--muted);text-align:justify;width:265px}
.name{font-size:15px;font-weight:500}
.stars{color:var(--star);font-size:16px;letter-spacing:1px}
.option{left:468px;width:264px;height:43px;border-radius:22px;background:#fff;box-shadow:0 3px 10px rgba(20,30,60,.06);display:flex;align-items:center;justify-content:center;font-size:14px;font-weight:500}
.footer{left:0;top:2963px;width:1200px;height:332px;background:var(--footer);color:#fff}
.f-head{font-size:16px;font-weight:700}
.f-list{list-style:none;font-size:13px;line-height:24px}
.social{width:30px;height:30px;border-radius:50%;border:1.5px solid #fff}
.contact-label{font-size:11px;font-weight:700}
.contact-value{font-size:13px;line-height:17px}
</style>
</head>
<body>

<svg class="bg-shapes" viewBox="0 0 1200 3295" aria-hidden="true">
  <polygon points="0,0 1200,0 1200,620 960,520 230,680 0,640" fill="#f3f5f9"/>
  <polygon points="0,575 245,672 165,696 0,635" fill="#0a84f0"/>
  <polygon points="1010,560 1100,512 1200,560 1200,640" fill="#0a84f0"/>
  <polygon points="0,1090 280,1210 960,1040 1200,1120 1200,1802 0,1802" fill="#f3f5f9"/>
  <polygon points="958,1052 1050,1034 1200,1100 1200,1158" fill="#0a84f0"/>
  <polygon points="0,1088 185,1172 112,1216 0,1170" fill="#0a84f0"/>
  <polygon points="0,2380 240,2290 1000,2380 1200,2330 1200,2963 0,2963" fill="#f3f5f9"/>
  <polygon points="0,2330 160,2258 242,2290 0,2392" fill="#0a84f0"/>
  <polygon points="1028,2470 1150,2398 1200,2420 1200,2532" fill="#0a84f0"/>
  <circle cx="173" cy="2425" r="6" fill="#e8463a"/>
  <circle cx="368" cy="2448" r="6" fill="#f0c24a"/>
  <circle cx="288" cy="2494" r="9" fill="none" stroke="#e8463a" stroke-width="1.5"/>
  <circle cx="33" cy="2531" r="6" fill="#a89ee0"/>
  <circle cx="176" cy="2601" r="9" fill="none" stroke="#a89ee0" stroke-width="1.5"/>
  <circle cx="1095" cy="2449" r="9" fill="none" stroke="#a89ee0" stroke-width="1.5"/>
  <circle cx="1184" cy="2448" r="6" fill="#f0c24a"/>
  <circle cx="1076" cy="2530" r="6" fill="#e8463a"/>
  <circle cx="462" cy="2960" r="9" fill="none" stroke="#a89ee0" stroke-width="1.5"/>
</svg>

<header>
  <div class="abs logo" style="left:143px;top:49px">Harbor Agent</div>
  <nav class="abs nav-links"><span>Home</span><span>How it Works</span><span>Blog</span><span>Contact Us</span></nav>
  <div class="abs login">Log In</div>
  <div class="abs btn-dark">Get Started</div>
</header>

<section class="hero">
  <h1 class="abs hero-title">Buy your next home<br><span class="hl">before you sell</span></h1>
  <p class="abs hero-text">Lorem ipsum dolor sit amet, consectetur adipiscing elit, sed incididunt ut labore et dolore magna aliqua.</p>
  <div class="abs btn-blue" style="left:145px;top:394px;width:180px;height:49px;font-size:16px">GET STARTED</div>
  <div class="abs" role="img" aria-label="Illustration of a two-storey house with a for sale sign, trees and sun" style="left:590px;top:130px;width:610px;height:300px;border-radius:190px 0 0 0;background:linear-gradient(180deg,var(--sky) 0%,#dfe6f4 58%,var(--leaf) 72%,#9fc4a3 84%,var(--lilac) 100%)"></div>
</section>

<section class="about">
  <div class="abs" role="img" aria-label="Illustration of a realtor shaking hands with a couple in front of houses for sale" style="left:8px;top:775px;width:545px;height:280px;border-radius:24px;background:linear-gradient(180deg,#f1f5fb 0%,var(--sky-deep) 55%,#eef2f8 100%)"></div>
  <h2 class="abs section-title" style="left:623px;top:700px;font-size:34px">Your Harbor <span class="hl">Agent</span></h2>
  <p class="abs about-text" style="top:763px">Lorem ipsum dolor sit amet, consectetur adipiscing elit, sed do eius-mod tempor incididunt ut labore et dolore magna aliqua. Ut enim ad minim veniam, quis nostrud exercitation ullamco laboris nisi ut aliquip ex ea commodo consequat.</p>
  <p class="abs about-text" style="top:866px">Duis aute irure dolor in reprehenderit in voluptate velit esse cillum dolore eu fugiat nulla pariatur.</p>
  <div class="abs btn-blue" style="left:623px;top:947px;width:154px;height:40px;font-size:13px">READ MORE
    <svg width="12" height="12" viewBox="0 0 12 12"><circle cx="6" cy="6" r="6" fill="#fff"/><path d="M5 3.5 7.5 6 5 8.5" stroke="#0a84f0" stroke-width="1.6" fill="none"/></svg></div>
</section>

<section class="features">
  <h2 class="abs section-title" style="left:0;width:1200px;text-align:center;top:1232px;font-size:36px">Key Features &amp; <span class="hl">Benefits</span></h2>
  <div class="abs" role="img" aria-label="Illustration of a realtor handing keys to a couple outside a house" style="left:440px;top:1328px;width:320px;height:320px;border-radius:50%;background:linear-gradient(180deg,#c9c6d6 0%,#ddd8e3 55%,#e7b451 80%,#b9b4c4 100%)"></div>

  <div class="abs feature" style="right:857px;top:1353px">Magically Convenient</div>
  <div class="abs icon-badge" style="left:358px;top:1326px"><svg width="38" height="38" viewBox="0 0 38 38" fill="none" stroke="#1c2a4a" stroke-width="1.6"><circle cx="20" cy="14" r="10"/><path d="M15 14l4 4 7-8" stroke="#0a84f0"/><path d="M4 28h10l8 3 10-5"/></svg></div>

  <div class="abs feature" style="right:891px;top:1477px">Integrated services</div>
  <div class="abs icon-badge" style="left:326px;top:1450px"><svg width="38" height="38" viewBox="0 0 38 38" fill="none" stroke="#1c2a4a" stroke-width="1.6"><path d="M4 18l8-8 7 4 7-4 8 8-10 10-5-5"/><path d="M12 22l5 5"/></svg></div>

  <div class="abs feature" style="right:857px;top:1602px">Price-boosting options</div>
  <div class="abs icon-badge" style="left:358px;top:1575px"><svg width="38" height="38" viewBox="0 0 38 38" fill="none" stroke="#1c2a4a" stroke-width="1.6"><rect x="5" y="6" width="22" height="26" rx="2"/><path d="M9 13h10M9 19h8M9 25h6"/><circle cx="27" cy="25" r="7" stroke="#0a84f0"/></svg></div>

  <div class="abs icon-badge" style="left:767px;top:1326px"><svg width="38" height="38" viewBox="0 0 38 38" fill="none" stroke="#1c2a4a" stroke-width="1.6"><path d="M6 18L19 6l13 12v14H6z"/><path d="M12 24l5 4 9-8" stroke="#0a84f0"/></svg></div>
  <div class="abs feature" style="left:858px;top:1353px">Local agents</div>

  <div class="abs icon-badge" style="left:800px;top:1450px"><svg width="38" height="38" viewBox="0 0 38 38" fill="none" stroke="#1c2a4a" stroke-width="1.6"><circle cx="19" cy="11" r="4"/><path d="M9 30l4-12h12l4 12z"/><path d="M6 8l3 3M32 8l-3 3" stroke="#0a84f0"/></svg></div>
  <div class="abs feature" style="left:891px;top:1477px">Stress-free certainty</div>

  <div class="abs icon-badge" style="left:767px;top:1575px"><svg width="38" height="38" viewBox="0 0 38 38" fill="none" stroke="#1c2a4a" stroke-width="1.6"><path d="M5 18L19 6l14 12"/><rect x="9" y="17" width="20" height="15"/><rect x="12" y="21" width="8" height="6" stroke="#0a84f0"/></svg></div>
  <div class="abs feature" style="left:858px;top:1602px">Skip the showings</div>

  <div class="abs btn-blue" style="left:524px;top:1677px;width:153px;height:41px;font-size:13px">LEARN MORE
    <svg width="12" height="12" viewBox="0 0 12 12"><circle cx="6" cy="6" r="6" fill="#fff"/><path d="M5 3.5 7.5 6 5 8.5" stroke="#0a84f0" stroke-width="1.6" fill="none"/></svg></div>
</section>

<section class="stories">
  <h2 class="abs section-title" style="left:0;width:1200px;text-align:center;top:1882px;font-size:36px">Success <span class="hl">Stories</span></h2>

  <article class="abs card" style="left:193px;top:1961px"></article>
  <div class="abs card-photo" role="img" aria-label="Photo of a happy family at home" style="left:144px;top:2015px;background:linear-gradient(135deg,#c8a27a,#6b4a35)"></div>
  <div class="abs hl quote-mark" style="left:288px;top:1982px">“</div>
  <p class="abs quote-text" style="left:289px;top:2031px">Lorem ipsum dolor sit amet, consectetur adipiscing elit, sed do eiusmod tempor labore et dolore magna aliqua.</p>
  <div class="abs name" style="left:289px;top:2111px">Sam Rivera</div>
  <div class="abs stars" style="left:288px;top:2129px">★★★★★</div>

  <article class="abs card" style="left:675px;top:1961px"></article>
  <div class="abs card-photo" role="img" aria-label="Photo of parents relaxing with their children" style="left:627px;top:2015px;background:linear-gradient(135deg,#d9c4b0,#7d6557)"></div>
  <div class="abs hl quote-mark" style="left:770px;top:1982px">“</div>
  <p class="abs quote-text" style="left:771px;top:2031px">Lorem ipsum dolor sit amet, consectetur adipiscing elit, sed do eiusmod tempor labore et dolore magna aliqua.</p>
  <div class="abs name" style="left:771px;top:2111px">Sam Rivera</div>
  <div class="abs stars" style="left:770px;top:2129px">★★★★★</div>
</section>

<section class="lead-form">
  <div class="abs" role="img" aria-label="Illustration of light blue houses with trees" style="left:0;top:2600px;width:420px;height:330px;border-radius:0 140px 0 0;background:linear-gradient(180deg,#dce8f7 0%,#b8d4f3 45%,#9cc4f0 80%,var(--lilac) 100%)"></div>
  <div class="abs" role="img" aria-label="Illustration of blue houses and city towers with green trees" style="left:770px;top:2480px;width:430px;height:450px;border-radius:180px 0 0 0;background:linear-gradient(180deg,#dbe7f7 0%,#a9c8f2 30%,#3b8fe8 62%,#78ad84 86%,var(--lilac) 100%)"></div>

  <h2 class="abs section-title" style="left:0;width:1200px;text-align:center;top:2462px;font-size:36px">The better way to <span class="hl">buy and sell</span></h2>
  <div class="abs" style="left:0;width:1200px;text-align:center;top:2543px;font-size:23px;font-weight:500">Are you:</div>
  <div class="abs option" style="top:2597px">Just buying</div>
  <div class="abs option" style="top:2656px">Just selling</div>
  <div class="abs option" style="top:2715px">Both</div>
  <div class="abs btn-blue" style="left:468px;top:2801px;width:264px;height:43px;font-size:14px;font-weight:500">Next</div>
</section>

<footer class="abs footer">
  <div class="abs logo" style="left:165px;top:92px;font-size:30px;color:#fff">Harbor Agent</div>
  <div class="abs" style="left:202px;top:140px;display:flex;gap:8px" aria-label="Social links">
    <span class="social"></span><span class="social"></span><span class="social"></span><span class="social"></span>
  </div>

  <div class="abs f-head" style="left:473px;top:55px">Quick Links</div>
  <ul class="abs f-list" style="left:474px;top:94px"><li>Home</li><li>How it Works</li><li>Blog</li><li>Benifits</li><li>Contact Us</li></ul>

  <div class="abs f-head" style="left:643px;top:55px">About Company</div>
  <ul class="abs f-list" style="left:644px;top:94px"><li>Legal Information</li><li>Terms &amp; Condition</li><li>Privacy Policy</li><li>Support</li><li>Site Map</li></ul>

  <div class="abs f-head" style="left:834px;top:55px">Contact Us</div>
  <svg class="abs" style="left:832px;top:97px" width="13" height="13" viewBox="0 0 24 24"><path fill="#0a84f0" d="M6.6 10.8a15 15 0 006.6 6.6l2.2-2.2c.3-.3.7-.4 1-.2 1.1.4 2.3.6 3.6.6.6 0 1 .4 1 1V20c0 .6-.4 1-1 1A17 17 0 013 4c0-.6.4-1 1-1h3.5c.6 0 1 .4 1 1 0 1.3.2 2.5.6 3.6.1.3 0 .7-.2 1z"/></svg>
  <div class="abs contact-label" style="left:855px;top:97px">Phone</div>
  <div class="abs contact-value" style="left:855px;top:114px">+1-555-014-2290</div>
  <svg class="abs" style="left:830px;top:144px" width="15" height="12" viewBox="0 0 15 12"><rect width="15" height="12" rx="1.5" fill="#0a84f0"/><path d="M1 1.5l6.5 5 6.5-5" stroke="#070b1f" stroke-width="1.3" fill="none"/></svg>
  <div class="abs contact-label" style="left:856px;top:144px">Email</div>
  <div class="abs contact-value" style="left:858px;top:166px">hello@harboragent.example</div>
  <svg class="abs" style="left:833px;top:193px" width="10" height="14" viewBox="0 0 10 14"><path d="M5 0a5 5 0 015 5c0 4-5 9-5 9S0 9 0 5a5 5 0 015-5z" fill="#0a84f0"/><circle cx="5" cy="5" r="2" fill="#070b1f"/></svg>
  <div class="abs contact-label" style="left:855px;top:194px">Location</div>
  <div class="abs contact-value" style="left:855px;top:212px">482 Maple Crest Road, Suite 12<br>Lakeview, CO 80011</div>

  <div class="abs" style="left:145px;top:274px;width:912px;height:1px;background:#3a3f55"></div>
  <div class="abs" style="left:1116px;top:258px;width:32px;height:32px;border-radius:50%;background:#fff;display:flex;align-items:center;justify-content:center"><svg width="12" height="8" viewBox="0 0 12 8"><path d="M1 7l5-5 5 5" stroke="#070b1f" stroke-width="1.8" fill="none"/></svg></div>
  <div class="abs" style="left:0;width:1200px;text-align:center;top:298px;font-size:14px">2024 Copyright - &nbsp;Harbor Agent &nbsp; | &nbsp; All Rights Reserved</div>
</footer>

</body>
</html>
```